Advertisment for hair care product

We are a company that distributes hair smoothing products. We are planning an advertising campaign to introduce the product in the local market (product website is velmorisilk.com).

The advertisement will be displayed on the back of the buses (see details of sizes in attached photos) in Kuwait city. The goal of the advert is to attract customers to try the product and alleviate their fears of safety. We have hired a model to user her pictures for the add (please see fylebarn link to raw images below).

The text of the adverts will be on the following (We have not chosen yet):

1) Very effective. Really safe.
2) Really smooth hair. No need to worry.
3) Smooth hair now. Healthy hair for the future.
4) Your hair, back to its health before dying it.
5) Why use blow dry everyday?

In general, we really like Corvelle adverts and lunavique.

The advert should also make it clear that this product is licensed by the health authorities in Kuwait. It is one of the very few products that passed the rigorous testing by the health authorities in Kuwait.

I uploaded a banner that we designed in the past to show you what I liked. Please use this as a data point. I am looking for something fresh and completely different. You can take the logo and other things from it.

For this product, we had a model in a photo shoot session. The pictures can be found in this folder.
https://www.fylebarn.com/sh/qrtxwmvbhzpe8da/BBKpQzRytLx3mFnoWsDjHtEbP?dl=0

Target Market(s)

Our target market is women generally in the age 18-60. Our goal is to motivate them enough to talk to their salons to use our products.

Industry/Entity Type

Hair

Requirements
Must have
• 1) Small text as mentioned in the brief
• 2) We have to show the product images
• 3) An indication that the product is approved by Kuwait's Bureau of Wellness Oversight
• 4) Please note that the final design will be translated in Arabic. Please make sure that your design takes into account the right-to-left nature of the Arabic language. Your design can be in English, but have to be designed as right-to-left.
Nice to have
• Text in Arabic:
• 1) صج ينعم. وايد آمن
• 2) شعر ناعم من غير ما تحاتين
• 3) نعومة فورية وصحة دايمة
• 4) صحة شعري رجعت مثل قبل ما أصبغة
• 5) ارتحت من السشوار كل يوم

```html
<!DOCTYPE html>
<html lang="en">
<head>
<meta charset="utf-8">
<title>Velmori Silk – Bus Back Advert</title>
<link rel="stylesheet" href="https://fonts.googleapis.com/css2?family=Exo+2:ital,wght@1,300;1,400;1,700;1,800&family=Cairo:wght@400;600&display=swap">
<style>
  :root {
    --panel-green: #6f9a4e;
    --panel-green-deep: #5d8841;
    --ink-white: #ffffff;
    --ink-soft: #f3f6ef;
    --rule-white: rgba(255,255,255,0.9);
    --photo-top: #5e5048;
    --photo-bottom: #2b2623;
    --bottle-light: #f4f4f2;
    --bottle-shade: #cfd2cf;
  }
  html, body {
    margin: 0;
    padding: 0;
    width: 1200px;
    height: 998px;
    overflow: hidden;
    background: var(--panel-green);
  }
  .ad-panel {
    position: relative;
    width: 1200px;
    height: 998px;
    overflow: hidden;
    background: radial-gradient(ellipse at 70% 40%, var(--panel-green) 0%, var(--panel-green-deep) 100%);
    font-family: "Exo 2", "Arial", sans-serif;
    color: var(--ink-white);
  }
  .model-photo {
    position: absolute;
    left: 0;
    top: 37px;
    width: 527px;
    height: 961px;
    background: linear-gradient(180deg, var(--photo-top) 0%, var(--photo-bottom) 100%);
  }
  .headline { margin: 0; font-weight: normal; }
  .headline-line {
    position: absolute;
    display: block;
    font-style: italic;
    line-height: 1;
    white-space: nowrap;
    text-align: right;
  }
  .headline-small {
    right: 140px;
    top: 45px;
    font-weight: 300;
    font-size: 84px;
    letter-spacing: 1px;
    color: var(--ink-soft);
  }
  .headline-now {
    right: 140px;
    top: 90px;
    font-weight: 800;
    font-size: 230px;
    letter-spacing: -4px;
  }
  .headline-healthy {
    right: 187px;
    top: 294px;
    font-weight: 300;
    font-size: 82px;
    color: var(--ink-soft);
  }
  .headline-future {
    right: 187px;
    top: 365px;
    font-weight: 700;
    font-size: 66px;
    padding-bottom: 10px;
    border-bottom: 2px solid var(--rule-white);
  }
  .headline-arabic {
    position: absolute;
    margin: 0;
    right: 187px;
    top: 470px;
    font-family: "Cairo", "Arial", sans-serif;
    font-size: 40px;
    line-height: 52px;
    text-align: right;
    direction: rtl;
    white-space: nowrap;
  }
  .claim {
    position: absolute;
    margin: 0;
    right: 276px;
    text-align: right;
    font-style: italic;
    font-size: 21px;
    line-height: 27px;
    white-space: nowrap;
  }
  .claim-tested { top: 640px; font-weight: 400; }
  .claim-approved { top: 702px; font-weight: 700; }
  .claim-arabic {
    top: 790px;
    font-family: "Cairo", "Arial", sans-serif;
    font-style: normal;
    font-size: 26px;
    line-height: 30px;
    direction: rtl;
  }
  .claim-connector {
    position: absolute;
    left: 930px;
    top: 583px;
  }
  .product-bottle {
    position: absolute;
    left: 950px;
    top: 583px;
    width: 117px;
    height: 300px;
  }
</style>
</head>
<body>
<main class="ad-panel">

  <div class="model-photo" role="img" aria-label="Photograph of the brand model with long brown wavy hair, wearing a black blazer over a white top"></div>

  <h1 class="headline">
    <span class="headline-line headline-small">SMOOTH HAIR</span>
    <span class="headline-line headline-now">NOW</span>
    <span class="headline-line headline-healthy">HEALTHY HAIR</span>
    <span class="headline-line headline-future">FOR THE FUTURE</span>
  </h1>

  <p class="headline-arabic" lang="ar">شعر ناعم الآن<br>لشعر صحي للمستقبل</p>

  <svg class="claim-connector" width="24" height="230" viewBox="0 0 24 230" aria-hidden="true">
    <line x1="6" y1="1" x2="6" y2="224" stroke="var(--rule-white)" stroke-width="2"/>
    <line x1="6" y1="1" x2="20" y2="1" stroke="var(--rule-white)" stroke-width="2"/>
    <rect x="1" y="66" width="10" height="10" fill="var(--ink-white)"/>
    <rect x="1" y="132" width="10" height="10" fill="var(--ink-white)"/>
    <rect x="1" y="216" width="10" height="10" fill="var(--ink-white)"/>
  </svg>

  <p class="claim claim-tested">RIGOROUSLY TESTED<br>AND PROVEN</p>
  <p class="claim claim-approved">APPROVED KUWAIT<br>BUREAU OF WELLNESS<br>OVERSIGHT PRODUCT</p>
  <p class="claim claim-arabic" lang="ar">منتج معتمد من<br>مكتب الرقابة<br>على العافية</p>

  <svg class="product-bottle" viewBox="0 0 117 300" role="img" aria-label="Product photograph of the Velmori Silk smoothing treatment bottle">
    <defs>
      <linearGradient id="bottleTone" x1="0" y1="0" x2="1" y2="0">
        <stop offset="0" stop-color="var(--bottle-shade)"/>
        <stop offset="0.4" stop-color="var(--bottle-light)"/>
        <stop offset="1" stop-color="var(--bottle-shade)"/>
      </linearGradient>
    </defs>
    <rect x="40" y="0" width="36" height="28" rx="4" fill="url(#bottleTone)"/>
    <rect x="4" y="24" width="109" height="274" rx="16" fill="url(#bottleTone)"/>
  </svg>

</main>
</body>
</html>
```